Etiketten-Design für Nahrungsergänzungsmittel
Zielgruppe
Die Firma vertreibt Nahrungsergänzungsmittel, gesunde Lebensmittel, Lifestyle und Wellnessprodukte. Dies vor allem im Fitness und Sport Bereich. Die Marke und das entsprechende Logo sollen auf eine jüngere Zielgruppe 25+ ausgerichtet sein. Personen die für Ihren Körper und Gesundheit Sport treiben und zusätzlich Unterstützung benötigen. Die Produkte werden über Pixoria durch eine Fitnesstrainerin beworben, und hauptsächlich über Velbro vertrieben. Produkte sind z. B. Produkte zur Ausdauersteigerung, verbesserte Konzentration, Schlaf, Stressbewältigung. Protein Shakes oder Vitamine für Veganer. No gos, Diät Produkte 5kg in 3 Tagen, Potenzsteigerung, Brustvergrößerung oder ähnliches.
Aufgabenstellung
Das Etikett wird auf einen wiederverschließbaren schwarz matten Kraftpapier Beutel im Format 28x20cm aufgebracht. Der Beutel und auch das Etikett sind kompostierbar, sieht aber beides hochwertig aus. Das Produkt ist ein veganes Proteinpulver zum anrühren mit Wasser oder Milchalternative. Einen ersten Entwurf habe ich hochgeladen.

```html
<!DOCTYPE html>
<html lang="de">
<head>
<meta charset="utf-8">
<title>LUMA Veganer Protein Shake – Etikett</title>
<link rel="stylesheet" href="https://fonts.googleapis.com/css2?family=Open+Sans:wght@400;600;800&family=Orbitron:wght@600&family=Teko:wght@500&family=Yanone+Kaffeesatz:wght@400&display=swap">
<style>
  :root {
    --bg: #232323;
    --panel-dark: #1e1c1d;
    --teal: #14a39a;
    --white: #ffffff;
    --cream: #f6e6c3;
    --ink: #1a1a1a;
    --divider: #f2f2f2;
  }
  * { margin: 0; padding: 0; box-sizing: border-box; }
  html, body { width: 1200px; height: 857px; overflow: hidden; background: var(--bg); }
  .label { position: relative; width: 1200px; height: 857px; background: var(--bg); font-family: "Open Sans", sans-serif; color: var(--white); }
  .divider { position: absolute; left: 597px; top: 0; width: 4px; height: 857px; background: var(--divider); }

  /* front */
  .brand-dot { position: absolute; left: 302px; top: 133px; width: 44px; height: 44px; border-radius: 50%; background: var(--teal); }
  .brand-box { position: absolute; left: 113px; top: 363px; width: 422px; height: 119px; background: var(--panel-dark); display: flex; align-items: center; justify-content: center; }
  .brand-name { font-family: "Open Sans", sans-serif; font-weight: 800; font-size: 122px; line-height: 1; letter-spacing: 6px; color: var(--white); }
  .product-name { position: absolute; left: 0; top: 528px; width: 596px; text-align: center; font-family: "Orbitron", sans-serif; font-weight: 600; font-size: 64px; line-height: 87px; letter-spacing: 8px; color: var(--teal); }

  /* back */
  .back { position: absolute; left: 628px; top: 0; width: 572px; height: 857px; }
  .back p { font-size: 16.5px; line-height: 17px; color: var(--white); }
  .description { position: absolute; left: 0; top: 32px; width: 550px; }
  .ingredients { position: absolute; left: 0; top: 94px; width: 480px; }
  .section-title { font-family: "Teko", sans-serif; font-weight: 500; font-size: 24px; letter-spacing: 2px; line-height: 1; color: var(--white); position: absolute; }

  .nutrition { position: absolute; left: 0; top: 219px; border-collapse: separate; border-spacing: 4px 4px; margin-left: -4px; margin-top: -4px; }
  .nutrition td { height: 23.5px; font-size: 13.5px; color: var(--ink); background: var(--white); padding: 0 4px; }
  .nutrition tr:nth-child(odd) td { background: var(--cream); }
  .nutrition td.value { text-align: center; width: 110px; }
  .nutrition td.name { width: 216px; }
  .nutrition tr.energy td { height: 30px; line-height: 14px; }

  .amino { position: absolute; left: 0; top: 477px; border-collapse: separate; border-spacing: 3px 2px; margin-left: -3px; }
  .amino td { height: 19.8px; font-size: 16px; color: var(--ink); background: var(--white); padding: 0 4px; line-height: 1; }
  .amino tr:nth-child(odd) td { background: var(--cream); }
  .amino td.aa { width: 85px; }
  .amino td.amt { width: 55px; text-align: center; }

  .usage { position: absolute; left: 4px; top: 627px; width: 200px; font-size: 15px !important; line-height: 15.3px !important; }
  .company { position: absolute; left: 0; top: 776px; font-size: 17px !important; }
  .greeting { position: absolute; left: 207px; top: 624px; font-family: "Yanone Kaffeesatz", sans-serif; font-size: 23px; line-height: 28px; color: var(--teal); }
  .social { position: absolute; left: 207px; top: 692px; display: flex; align-items: center; gap: 20px; }
  .social-dot { width: 34px; height: 34px; border-radius: 50%; background: var(--teal); }
  .social-handle { font-size: 22px; color: var(--teal); }
  .contents { position: absolute; left: 205px; top: 742px; }

  .art { position: absolute; }
  .art-vanilla { left: 1075px; top: 112px; width: 105px; height: 84px; border-radius: 40%; background: radial-gradient(circle, #f7d977 0%, #f2e3a4 55%, rgba(35,35,35,0) 72%); }
  .art-peas { left: 1095px; top: 230px; width: 85px; height: 100px; border-radius: 45%; background: radial-gradient(circle, #6ab23f 0%, #3f8a2c 55%, rgba(35,35,35,0) 74%); }
  .art-pumpkin { left: 1105px; top: 372px; width: 66px; height: 78px; border-radius: 45%; background: radial-gradient(circle, #4a9a3a 0%, #c8b98a 55%, rgba(35,35,35,0) 74%); }
  .art-rice { left: 1095px; top: 490px; width: 85px; height: 80px; border-radius: 45%; background: radial-gradient(circle, #f0f0f0 0%, #cfcfcf 50%, rgba(35,35,35,0) 72%); }
  .photo-trainer { left: 1040px; top: 608px; width: 160px; height: 249px; border-radius: 70px 70px 0 0; background: linear-gradient(180deg, #c9a37d 0%, #d8a88a 30%, #5f8fa1 55%, #2a2a2e 100%); }
</style>
</head>
<body>
<main class="label">
  <section class="front">
    <div class="brand-dot"></div>
    <div class="brand-box"><span class="brand-name">LUMA</span></div>
    <h1 class="product-name">VEGANER<br>PROTEIN<br>SHAKE</h1>
  </section>

  <div class="divider"></div>

  <section class="back">
    <p class="description">Getränkepulver zur Herstellung eines veganen Eiweißgetränkes mit Süßungsmittel - Geschmacksrichtung Vanille</p>
    <p class="ingredients">Zutaten: Eiweißmischung (93 %) Erbseneiweiß, Reiseiweiß, Hanfsamenpulver, Bio Kürbiskerneiweiß, Aroma, Verdickungsmittel: Xanthan, Kokosnussmilchpulver, Süßungsmittel: Sucralose</p>

    <h2 class="section-title" style="left:0;top:196px;">NÄHRWERTANGABEN PRO</h2>
    <h2 class="section-title" style="left:248px;top:199px;">100G</h2>
    <h2 class="section-title" style="left:342px;top:199px;">PORTION = 30G</h2>

    <table class="nutrition">
      <tr class="energy"><td class="name">Energie</td><td class="value">1.9694 kJ<br>401 kcal</td><td class="value">1.9694 kJ<br>401 kcal</td></tr>
      <tr><td class="name">- davon gesättigte Fettsäuren</td><td class="value">8,3 g</td><td class="value">8,3 g</td></tr>
      <tr><td class="name">Kohlenhydrate</td><td class="value">8,3 g</td><td class="value">8,3 g</td></tr>
      <tr><td class="name">- davon Zucker</td><td class="value">8,3 g</td><td class="value">8,3 g</td></tr>
      <tr><td class="name">Ballaststoffe</td><td class="value">8,3 g</td><td class="value">8,3 g</td></tr>
      <tr><td class="name">Eiweiß</td><td class="value">8,3 g</td><td class="value">8,3 g</td></tr>
      <tr><td class="name">Salz</td><td class="value">8,3 g</td><td class="value">8,3 g</td></tr>
      <tr><td class="name">Fett</td><td class="value">8,3 g</td><td class="value">8,3 g</td></tr>
    </table>

    <h2 class="section-title" style="left:0;top:452px;">AMINOSÄURENPROFIL PRO 100G EIWEISS</h2>

    <table class="amino">
      <tr><td class="aa">Eiweiß</td><td class="amt">4,4 g</td><td class="aa">Eiweiß</td><td class="amt">4,4 g</td><td class="aa">Eiweiß</td><td class="amt">4,4 g</td></tr>
      <tr><td class="aa">Eiweiß</td><td class="amt">4,4 g</td><td class="aa">Eiweiß</td><td class="amt">4,4 g</td><td class="aa">Eiweiß</td><td class="amt">4,4 g</td></tr>
      <tr><td class="aa">Eiweiß</td><td class="amt">4,4 g</td><td class="aa">Eiweiß</td><td class="amt">4,4 g</td><td class="aa">Eiweiß</td><td class="amt">4,4 g</td></tr>
      <tr><td class="aa">Eiweiß</td><td class="amt">4,4 g</td><td class="aa">Eiweiß</td><td class="amt">4,4 g</td><td class="aa">Eiweiß</td><td class="amt">4,4 g</td></tr>
      <tr><td class="aa">Eiweiß</td><td class="amt">4,4 g</td><td class="aa">Eiweiß</td><td class="amt">4,4 g</td><td class="aa">Eiweiß</td><td class="amt">4,4 g</td></tr>
      <tr><td class="aa">Eiweiß</td><td class="amt">4,4 g</td><td class="aa">Eiweiß</td><td class="amt"></td><td class="aa">Eiweiß</td><td class="amt">4,4 g</td></tr>
    </table>

    <p class="usage">Verzehrempfehlung:<br>30 g Pulver im 300 ml Wasser lösen; Das Produkt ist kühl, trocken und dunkel zu lagern.</p>
    <p class="company">LUMA UG<br>Lindenallee 12<br>75001 Talheim<br>info@lumabyluma.de</p>

    <div class="greeting">Besuche mich auf Pixoria!<br>liebe Grüße Luma</div>
    <div class="social"><span class="social-dot"></span><span class="social-handle">lumabyluma</span></div>
    <p class="contents">Inhalt:<br>600 g Eiweißpulver<br>für 20 Shakes<br>Mindestens haltbar<br>bis Ende 08/2023<br>Losnr.: 977109</p>
  </section>

  <div class="art art-vanilla" role="img" aria-label="Illustration einer Vanilleblüte mit Vanilleschote"></div>
  <div class="art art-peas" role="img" aria-label="Illustration einer geöffneten Erbsenschote mit Erbsen"></div>
  <div class="art art-pumpkin" role="img" aria-label="Illustration von Kürbiskernen"></div>
  <div class="art art-rice" role="img" aria-label="Illustration von Reiskörnern"></div>
  <div class="art photo-trainer" role="img" aria-label="Foto der Fitnesstrainerin in Sportkleidung"></div>
</main>
</body>
</html>
```